Webdesign für Stahl- und Brückenbauunternehmen
Zielgruppe
Wir haben 180 Jahre Erfahrung im Stahl- und Brückenbau.
Unsere Auftraggeber ist die öffentliche Hand.
Aufgabenstellung
Das ODLA / TKU-Logo soll mit rein (siehe jetzige Webseite)

```html
<!DOCTYPE html>
<html lang="de">
<head>
<meta charset="utf-8">
<title>Norvek – Unsere Leistungen</title>
<link href="https://fonts.googleapis.com/css2?family=Poppins:wght@600;700&family=Questrial&display=swap" rel="stylesheet">
<style>
  :root {
    --brand-blue: #0a7cc8;
    --card-dark: #2b2a2f;
    --page-bg: #f4f5f8;
    --header-bg: #ffffff;
    --ink: #1f1f22;
    --ink-soft: #3a3a3f;
    --on-card: #ffffff;
    --divider-light: rgba(255,255,255,0.22);
  }
  * { box-sizing: border-box; margin: 0; padding: 0; }
  html, body {
    width: 719px; height: 1200px; overflow: hidden;
    background: var(--page-bg);
    font-family: "Questrial", "Century Gothic", sans-serif;
    color: var(--ink);
  }
  .site-header {
    height: 180px;
    background: var(--header-bg);
    display: flex; align-items: center; justify-content: space-between;
    padding: 0 38px 0 40px;
    box-shadow: 0 4px 0 #e6e8ec;
  }
  .brand-name {
    font-family: "Poppins", sans-serif;
    font-weight: 700;
    font-size: 64px;
    letter-spacing: 1px;
    color: var(--brand-blue);
  }
  .menu-button {
    width: 86px; height: 86px;
    background: #fff;
    border-radius: 14px;
    box-shadow: 0 4px 14px rgba(0,0,0,0.14);
    display: flex; align-items: center; justify-content: center;
  }
  .intro { padding: 50px 38px 0; }
  .intro-title {
    font-family: "Poppins", sans-serif;
    font-weight: 600;
    font-size: 38px;
    letter-spacing: 1.5px;
  }
  .intro-text {
    margin-top: 14px;
    font-size: 24px;
    line-height: 1.6;
    color: var(--ink-soft);
    max-width: 470px;
  }
  .services { padding: 40px 38px 0; display: flex; flex-direction: column; gap: 32px; }
  .service-card {
    height: 320px;
    border-radius: 14px;
    background: var(--card-dark);
    color: var(--on-card);
    padding: 28px 34px;
  }
  .service-card--featured { background: var(--brand-blue); }
  .service-head {
    display: flex; align-items: center; gap: 50px;
    padding-bottom: 24px;
    border-bottom: 1px solid var(--divider-light);
    margin-left: 0;
  }
  .service-icon {
    width: 98px; height: 98px;
    border-radius: 10px;
    background: #ffffff;
    flex: none;
  }
  .service-title {
    font-family: "Poppins", sans-serif;
    font-weight: 600;
    font-size: 32px;
    letter-spacing: 0.5px;
  }
  .service-text {
    margin-top: 26px;
    font-size: 25px;
    line-height: 1.7;
  }
</style>
</head>
<body>
  <header class="site-header">
    <div class="brand-name">Norvek</div>
    <div class="menu-button" aria-label="Menü">
      <svg width="44" height="36" viewBox="0 0 44 36">
        <rect x="0" y="0" width="44" height="6" rx="2" fill="#111"/>
        <rect x="0" y="15" width="44" height="6" rx="2" fill="#111"/>
        <rect x="0" y="30" width="44" height="6" rx="2" fill="#111"/>
      </svg>
    </div>
  </header>

  <section class="intro">
    <h1 class="intro-title">UNSERE LEISTUNGEN</h1>
    <p class="intro-text">Wir haben 180 Jahre Erfahrung im Stahl- und Brückenbau.</p>
  </section>

  <section class="services">
    <article class="service-card service-card--featured">
      <div class="service-head">
        <div class="service-icon" role="img" aria-label="Baustellen-Symbol"></div>
        <h2 class="service-title">Brücken</h2>
      </div>
      <p class="service-text">Die Fertigung umfasst unter anderem Brücken mit orthotroper Platte, Bogen-, Fachwerk-, Schrägseil- und Stahlverbundbrücken.</p>
    </article>

    <article class="service-card">
      <div class="service-head">
        <div class="service-icon" role="img" aria-label="Baustellen-Symbol"></div>
        <h2 class="service-title">VF-Träger</h2>
      </div>
      <p class="service-text">Die Fertigung umfasst unter anderem Brücken mit orthotroper Platte, Bogen-, Fachwerk-, Schrägseil- und Stahlverbundbrücken.</p>
    </article>

    <article class="service-card">
      <div class="service-head">
        <div class="service-icon" role="img" aria-label="Baustellen-Symbol"></div>
        <h2 class="service-title">Sonderstahlbau</h2>
      </div>
    </article>
  </section>
</body>
</html>
```